Wine label design

Need a logo/design for new wine label.
All we have is a label name which is "Marvonetta"
The vineyard is located on rocky hills but we dont really have any design concept in mind. We would like a fun but modern label.

Target Market(s)

Wine consumers. Not too serious. Premium quality product but should be fun and easy to recognise.

Industry/Entity Type

Vineyard

Colors

Designer to choose colors to be used in the design.

Requirements
Must have
• Simple, standout logo/label name
• Contemporary, modern, funky label
• Flexible on colour scheme. Would like it to stand-out and be recognisable but still needs an element of class that reflects premium quality wine.
Nice to have
• Potentially have a link to rolling hills of exposed rock that we produce from.
Should not have
• Old, traditional style label

```html
<!DOCTYPE html>
<html lang="en">
<head>
<meta charset="utf-8">
<title>Marvonetta – Wine Label</title>
<link rel="stylesheet" href="https://fonts.googleapis.com/css2?family=Poiret+One&display=swap">
<style>
  :root {
    --page: #f4f3f1;
    --band-black: #050505;
    --band-brown: #3b2226;
    --ink-light: #f2f2f2;
    --wine-red: #8c1520;
    --deep-red: #4a0c14;
    --teal: #3f8f8c;
    --slate: #3a3f4a;
    --smoke: #9a8f96;
  }
  * { margin: 0; padding: 0; box-sizing: border-box; }
  html, body {
    width: 1200px;
    height: 3629px;
    overflow: hidden;
    background: var(--page);
  }
  .canvas {
    position: relative;
    width: 1200px;
    height: 3629px;
  }
  .label {
    position: absolute;
    left: 100px;
    top: 814px;
    width: 1000px;
    height: 2000px;
    display: flex;
    flex-direction: column;
    background: var(--band-black);
  }
  .label__artwork {
    width: 100%;
  }
  .label__artwork--top {
    height: 893px;
    background:
      radial-gradient(circle at 25% 25%, var(--smoke) 0%, transparent 35%),
      radial-gradient(circle at 80% 30%, var(--teal) 0%, transparent 40%),
      radial-gradient(circle at 20% 75%, var(--wine-red) 0%, transparent 40%),
      radial-gradient(circle at 75% 80%, var(--deep-red) 0%, transparent 45%),
      linear-gradient(135deg, var(--slate), var(--deep-red));
  }
  .label__artwork--bottom {
    height: 766px;
    background:
      radial-gradient(circle at 25% 30%, var(--teal) 0%, transparent 40%),
      radial-gradient(circle at 30% 70%, var(--smoke) 0%, transparent 35%),
      radial-gradient(circle at 80% 40%, var(--wine-red) 0%, transparent 50%),
      linear-gradient(160deg, var(--slate), var(--wine-red) 60%, var(--deep-red));
  }
  .label__rule {
    height: 34px;
    background: var(--band-brown);
  }
  .label__nameplate {
    height: 307px;
    background: var(--band-black);
    display: flex;
    align-items: center;
    padding-left: 44px;
  }
  .label__name {
    font-family: "Poiret One", sans-serif;
    font-size: 190px;
    line-height: 1;
    color: var(--ink-light);
    letter-spacing: 0;
    text-transform: lowercase;
  }
</style>
</head>
<body>
  <main class="canvas">
    <section class="label">
      <div class="label__artwork label__artwork--top" role="img" aria-label="Abstract macro photograph of grapes and wine droplets in teal, slate and deep red"></div>
      <div class="label__rule"></div>
      <div class="label__nameplate">
        <h1 class="label__name">marvonetta</h1>
      </div>
      <div class="label__rule"></div>
      <div class="label__artwork label__artwork--bottom" role="img" aria-label="Abstract macro photograph of teal grapes and splashes of red wine"></div>
    </section>
  </main>
</body>
</html>
```